Boilerplate Management Organization Chart

"Our Management Approach is a deliberate step-by-step process and supports our Technical Approach detailed in proposal submission. The Management Approach covers all the human capital aspects for executing a contract—from contract award through to sustainment and/or transition of the contract to another company. It includes how we organize, hire, staff, train, and account for our contract employees—as well as their complete personal life-cycle management within the company."

We need this management approach to depict an amazing management process that demonstrates best practices of the project management body of knowledge. We need this vector image to be applicable to any proposal without making references to any other proposals. Generic names but using strong business language.
Updates

Thanks for all designs submitted thus far. Some have stuck to the original type of chart. We would like to see a completely different way to show the same information. It has to be able to be recognized and deciphered very quickly by people who might not necessarily want to look at it. It must draw them in and make it incredibly easy to distinguish a management approach that looks fresh, infallible, and easily implemented.

Target Market(s)

Federal space, Government organizations looking for procedural efficiencies,

Industry/Entity Type

Management

Requirements
Must have
• Must not take up more than 1/3 to 1/2 of printable page and be clear.
Should not have
• Not too much color, but should stick to some color palette of some interest.

```html
<!DOCTYPE html>
<html lang="en">
<head>
<meta charset="utf-8">
<title>Management Approach Process Chart</title>
<link href="https://fonts.googleapis.com/css2?family=Arimo:wght@700&family=Source+Sans+3:wght@600;700&display=swap" rel="stylesheet">
<style>
  :root {
    --canvas: #ffffff;
    --page: #ffffff;
    --page-edge: #d4d4d4;
    --blue-deep: #1b3c91;
    --blue-mid: #2456a8;
    --blue-light: #3d93d2;
    --blue-edge: #0e2a6b;
    --grey-light: #ececec;
    --grey-mid: #d9d9d9;
    --grey-dark: #c2c2c2;
    --grey-edge: #b8b8b8;
    --bracket: #9a9a9a;
    --ink: #111111;
    --measure: #d2233c;
  }
  * { box-sizing: border-box; margin: 0; padding: 0; }
  html, body { width: 1200px; height: 1000px; overflow: hidden; background: var(--canvas); }
  .canvas { position: relative; width: 1200px; height: 1000px; }

  .page {
    position: absolute; left: 338px; top: 157px; width: 523px; height: 685px;
    background: var(--page); border: 1px solid var(--page-edge);
    box-shadow: 2px 3px 4px rgba(0,0,0,0.25);
  }

  .title-box {
    position: absolute; display: flex; align-items: center; justify-content: center;
    text-align: center; color: #fff; font-family: "Arimo", Arial, sans-serif; font-weight: 700;
    background: linear-gradient(180deg, var(--blue-light) 0%, var(--blue-mid) 45%, var(--blue-deep) 100%);
    border: 2px solid var(--blue-edge);
    box-shadow: 2px 3px 4px rgba(0,0,0,0.35);
    overflow: hidden;
    text-shadow: 1px 1px 2px rgba(0,0,0,0.4);
  }
  .title-box::after {
    content: ""; position: absolute; left: -20%; right: -20%; top: 48%; height: 120%;
    border-radius: 50% 50% 0 0 / 30% 30% 0 0; background: var(--blue-deep); z-index: 0;
  }
  .title-box span { position: relative; z-index: 1; }
  .title-box--approach { left: 552px; top: 172px; width: 276px; height: 94px; font-size: 34px; line-height: 35px; }
  .title-box--evaluation { left: 413px; top: 767px; width: 379px; height: 58px; font-size: 34px; }

  .step {
    position: absolute; width: 207px; height: 74px;
    display: flex; align-items: center; justify-content: center; text-align: center;
    font-family: "Source Sans 3", "Myriad Pro", sans-serif; font-weight: 700;
    font-size: 21px; line-height: 24px; color: var(--ink);
    background: linear-gradient(180deg, var(--grey-light), var(--grey-mid));
    border: 1px solid var(--grey-edge);
    box-shadow: 1px 2px 3px rgba(0,0,0,0.2);
    overflow: hidden;
  }
  .step::after {
    content: ""; position: absolute; left: -30%; right: -30%; top: 45%; height: 120%;
    border-radius: 50% 50% 0 0 / 25% 25% 0 0; background: var(--grey-dark); z-index: 0;
  }
  .step span { position: relative; z-index: 1; }
  .col-left { left: 376px; }
  .col-right { left: 616px; }
  .row-1 { top: 427px; }
  .row-2 { top: 510px; }
  .row-3 { top: 593px; }
  .row-4 { top: 676px; }

  .flow { position: absolute; inset: 0; width: 1200px; height: 1000px; pointer-events: none; }
  .flow .arrow { fill: var(--blue-mid); stroke: var(--blue-edge); stroke-width: 1.2; }
  .flow .connector { fill: none; stroke: var(--blue-deep); stroke-width: 3; }
  .flow .bracket { fill: none; stroke: var(--bracket); stroke-width: 3; }
  .flow .measure { fill: none; stroke: var(--measure); stroke-width: 1; }
  .measure-label { font-family: "Source Sans 3", sans-serif; font-weight: 700; font-size: 10px; fill: var(--measure); }
</style>
</head>
<body>
<div class="canvas">
  <div class="page"></div>

  <svg class="flow" viewBox="0 0 1200 1000" aria-hidden="true">
    <!-- size markers -->
    <path class="measure" d="M540 127 H567 M540 127 l6 -4 M540 127 l6 4 M630 127 H660 M660 127 l-6 -4 M660 127 l-6 4"/>
    <text class="measure-label" x="599" y="131" text-anchor="middle">7.25 INCHI</text>
    <path class="measure" d="M311 440 V470 M311 440 l-4 6 M311 440 l4 6 M311 530 V560 M311 560 l-4 -6 M311 560 l4 -6"/>
    <text class="measure-label" transform="translate(315 500) rotate(-90)" text-anchor="middle">9.5 INCHI</text>

    <!-- brackets -->
    <path class="bracket" d="M388 399 H360 V777 H388"/>
    <path class="bracket" d="M820 399 H839 V777 H820"/>

    <!-- connector from approach to steps -->
    <path class="connector" d="M644 285 V371 H793 V390"/>
    <polygon class="arrow" points="782,387 805,387 793,405"/>

    <!-- down arrows right column -->
    <polygon class="arrow" points="625,490 655,490 640,517"/>
    <polygon class="arrow" points="625,575 655,575 640,602"/>
    <polygon class="arrow" points="625,660 655,660 640,688"/>

    <!-- left arrow -->
    <polygon class="arrow" points="612,698 612,726 588,712"/>

    <!-- up arrows left column -->
    <polygon class="arrow" points="546,687 576,687 561,659"/>
    <polygon class="arrow" points="546,601 576,601 561,573"/>
    <polygon class="arrow" points="546,515 576,515 561,487"/>
  </svg>

  <div class="title-box title-box--approach"><span>Management<br>Approach</span></div>

  <div class="step col-left row-1"><span>Sustainment /<br>Transition</span></div>
  <div class="step col-left row-2"><span>Benefits</span></div>
  <div class="step col-left row-3"><span>Retention /<br>Quality Of Life</span></div>
  <div class="step col-left row-4"><span>Professional<br>Development</span></div>

  <div class="step col-right row-1"><span>Responsibility<br>Fixed</span></div>
  <div class="step col-right row-2"><span>Management &amp;<br>Oversight</span></div>
  <div class="step col-right row-3"><span>Manning<br>The Team</span></div>
  <div class="step col-right row-4"><span>Training</span></div>

  <svg class="flow" viewBox="0 0 1200 1000" aria-hidden="true">
    <polygon class="arrow" points="625,490 655,490 640,517"/>
    <polygon class="arrow" points="625,575 655,575 640,602"/>
    <polygon class="arrow" points="625,660 655,660 640,688"/>
    <polygon class="arrow" points="612,698 612,726 588,712"/>
    <polygon class="arrow" points="546,687 576,687 561,659"/>
    <polygon class="arrow" points="546,601 576,601 561,573"/>
    <polygon class="arrow" points="546,515 576,515 561,487"/>
  </svg>

  <div class="title-box title-box--evaluation"><span>Program Evaluation</span></div>
</div>
</body>
</html>
```